Billboard for personal injury chiropractors office

We are a personal injury chiropractor clinic.
I need a Billboard with the company name as the dominating factor. Also a smaller picture or 2 of something creative, like a car accident or an arm in a cast off to the sides.
We Like something Clean and Simple and Eye Catching. Please make the picture Small and Off To The Side. The MAIN FOCUS areas are the… name Pell Chiropractic Clinic
At the top CAR ACCIDENT INJURY?
AND at the bottom our number 581-47-TORSO.
Dr.Marla T. Pell in bold somewhere with the word chiropractor under the doctors name in a text.

Im open to red lettering on white backgrounds, red on yellow backgrounds and I'm also open to reds blues white and yellow. I'd prefer yellow if used be across the bottom.

I am uploading a very rough draft of what we are after along with a screenshot of the tv commercial showing the yellow

DO NOT USE THE LOGO ON THE COMMERCIAL. I JUST WANT THE NAME TYPED LIKE ON SAMPLE BILLBOARD.

Industry/Entity Type

Chiropractic

Colors
0054AA
0677BA
7BADD7
CADEEF
E8F1F8
FFF300
FFF600
FEFA6F
FFFEC7
FFFEE8
EB3D1F
EC4F4E
F09395
F8D3D4
FCEDEE

Requirements
Must have
• Eye catching ,bold

```html
<!DOCTYPE html>
<html lang="en">
<head>
<meta charset="utf-8">
<title>Pell Chiropractic Clinic Billboard</title>
<link rel="stylesheet" href="https://fonts.googleapis.com/css2?family=Anton&family=Oswald:wght@600&family=Montserrat:wght@800&display=swap">
<style>
  :root {
    --page-bg: #b3b3b3;
    --board-blue: #172c6b;
    --board-red: #c8101a;
    --accent-yellow: #fff200;
    --headline-red: #d0141c;
    --name-white: #ffffff;
  }
  html, body {
    margin: 0;
    padding: 0;
    width: 1023px;
    height: 1200px;
    overflow: hidden;
    background: var(--page-bg);
  }
  .billboard {
    position: absolute;
    left: 32px;
    top: 460px;
    width: 960px;
    height: 280px;
    box-shadow: 4px 6px 10px rgba(0,0,0,0.35);
    display: flex;
    flex-direction: column;
  }
  .billboard__top {
    background: var(--board-blue);
    height: 186px;
    display: flex;
    flex-direction: column;
    align-items: center;
    justify-content: center;
    gap: 2px;
  }
  .billboard__headline {
    margin: 0;
    font-family: "Anton", sans-serif;
    font-size: 70px;
    line-height: 1;
    letter-spacing: -1px;
    color: var(--headline-red);
    -webkit-text-stroke: 10px var(--accent-yellow);
    paint-order: stroke fill;
  }
  .billboard__name {
    margin: 0;
    font-family: "Oswald", sans-serif;
    font-weight: 600;
    font-size: 66px;
    line-height: 1;
    color: var(--name-white);
    text-transform: uppercase;
    transform: scaleX(1.02);
  }
  .billboard__bottom {
    background: var(--board-red);
    flex: 1;
    display: flex;
    align-items: center;
    justify-content: center;
    gap: 30px;
  }
  .billboard__phone-icon {
    width: 72px;
    height: 72px;
  }
  .billboard__phone {
    font-family: "Montserrat", sans-serif;
    font-weight: 800;
    font-size: 72px;
    line-height: 1;
    color: var(--accent-yellow);
    letter-spacing: -1px;
  }
</style>
</head>
<body>
  <section class="billboard">
    <div class="billboard__top">
      <h1 class="billboard__headline">CAR ACCIDENT INJURY?</h1>
      <h2 class="billboard__name">Pell Chiropractic Clinic</h2>
    </div>
    <div class="billboard__bottom">
      <svg class="billboard__phone-icon" viewBox="0 0 64 64" aria-hidden="true">
        <path fill="#fff200" d="M14 6c3-2 6-1 7 2l5 10c1 3 0 5-2 7l-4 3c3 7 8 12 15 15l3-4c2-2 4-3 7-2l10 5c3 1 4 4 2 7l-4 5c-3 3-8 4-13 2C25 51 13 39 8 24c-2-5-1-10 2-13z"/>
        <path fill="none" stroke="#fff200" stroke-width="4" stroke-linecap="round" d="M34 16a14 14 0 0 1 14 14M35 6a24 24 0 0 1 23 23"/>
      </svg>
      <span class="billboard__phone">581-47-TORSO</span>
    </div>
  </section>
</body>
</html>
```